FB and Youtube banner design for HVAC company

I would like an appealing site page banner for business page on Facebook (851w x 315h pixels) and one for youtube (2560w x 1440h pixels) for hvac company. Business card design and logo are attached. Company name is Silver Birch Air Conditioning, Refrigeration, and Heating.

NOTE: I put the business cards and log up to see some of the artwork the company is using. It's not to replicate that in the banner images.

Target Market(s)

Interested business and homeowner visitors to Facebook business page and youtube channel page.

Industry/Entity Type

Hvac

Font styles to use
Sans Serif

Requirements
Must have
• See logo for color scheme.
Should not have
• This should not look like a business card. Think of what is typically the banner on a facebook business page and youtube channel.

```html
<!DOCTYPE html>
<html lang="en">
<head>
<meta charset="utf-8">
<title>Silver Birch HVAC Banner</title>
<link href="https://fonts.googleapis.com/css2?family=Michroma&family=Montserrat:wght@600;700;800&display=swap" rel="stylesheet">
<style>
  :root {
    --backdrop: #979694;
    --blue-light: #6fa3fb;
    --blue-mid: #3a7ef0;
    --blue-deep: #0d4fc9;
    --brand-blue: #0d47c4;
    --brand-orange: #ff6a00;
    --ink: #4a4a4a;
    --white: #ffffff;
  }
  * { margin: 0; padding: 0; box-sizing: border-box; }
  html, body { width: 1200px; height: 1200px; overflow: hidden; }
  body { background: var(--backdrop); position: relative; font-family: "Montserrat", sans-serif; }
  .banner {
    position: absolute; left: 89px; top: 411px; width: 1022px; height: 379px;
    overflow: hidden;
    box-shadow: 0 6px 24px rgba(0,0,0,0.35);
  }
  .banner__backdrop {
    position: absolute; inset: 0;
    background: linear-gradient(160deg, var(--blue-light) 0%, var(--blue-mid) 45%, var(--blue-deep) 100%);
  }
  .banner__disc {
    position: absolute; left: 255px; top: -73px; width: 524px; height: 524px;
    border-radius: 50%; background: var(--white);
    box-shadow: 0 0 30px rgba(0,30,90,0.35);
  }
  .brand {
    position: absolute; left: 0; right: 0; top: 110px;
    display: flex; align-items: center; justify-content: center; gap: 16px;
    margin-left: 36px; width: 966px; 
  }
  .brand__dot { width: 46px; height: 46px; border-radius: 50%; background: var(--brand-orange); }
  .brand__name {
    font-family: "Montserrat", sans-serif; font-weight: 800; font-size: 46px;
    color: var(--brand-blue); letter-spacing: -0.5px; line-height: 1;
  }
  .services {
    position: absolute; left: 0; right: 0; top: 203px; margin-left: 36px; width: 966px;
    text-align: center; font-family: "Michroma", sans-serif; font-size: 13.5px;
    color: var(--ink); line-height: 20px; letter-spacing: 1px;
  }
  .tagline {
    position: absolute; left: 314px; top: 287px; width: 393px; height: 28px;
    border-radius: 14px; background: var(--brand-orange);
    box-shadow: 0 3px 5px rgba(0,0,0,0.25);
    color: var(--white); font-weight: 700; font-size: 13.5px;
    display: flex; align-items: center; justify-content: center; letter-spacing: 0.2px;
  }
  .contact {
    position: absolute; left: 0; top: 323px; margin-left: 36px; width: 966px;
    display: flex; justify-content: center; align-items: center; gap: 6px;
    color: var(--ink); font-weight: 600; font-size: 14.5px; letter-spacing: 0.4px;
  }
  .contact__icon { width: 14px; height: 14px; }
  .contact__item { display: flex; align-items: center; gap: 6px; }
  .contact__item + .contact__item { margin-left: 4px; }
</style>
</head>
<body>
  <section class="banner">
    <div class="banner__backdrop" role="img" aria-label="Faceted blue low-poly geometric background"></div>
    <div class="banner__disc"></div>

    <div class="brand">
      <span class="brand__dot"></span>
      <span class="brand__name">SILVER BIRCH</span>
    </div>

    <p class="services">AIR CONDITIONING - REFRIGERATION<br>HEATING - ICE MACHINES</p>

    <div class="tagline">SERVICE YOU CAN COUNT ON. LIKE CLOCKWORK.</div>

    <div class="contact">
      <span class="contact__item">
        <svg class="contact__icon" viewBox="0 0 24 24" aria-hidden="true">
          <path fill="#ff6a00" d="M6.6 10.8a15.1 15.1 0 0 0 6.6 6.6l2.2-2.2a1 1 0 0 1 1-.25 11.4 11.4 0 0 0 3.6.57 1 1 0 0 1 1 1V20a1 1 0 0 1-1 1A17 17 0 0 1 3 4a1 1 0 0 1 1-1h3.5a1 1 0 0 1 1 1c0 1.25.2 2.45.57 3.57a1 1 0 0 1-.25 1z"/>
        </svg>
        555.204.7731
      </span>
      <span class="contact__item">
        <svg class="contact__icon" viewBox="0 0 24 24" aria-hidden="true">
          <g fill="none" stroke="#ff6a00" stroke-width="2">
            <circle cx="12" cy="12" r="9.5"/>
            <ellipse cx="12" cy="12" rx="4" ry="9.5"/>
            <line x1="2.5" y1="12" x2="21.5" y2="12"/>
            <line x1="4" y1="7" x2="20" y2="7"/>
            <line x1="4" y1="17" x2="20" y2="17"/>
          </g>
        </svg>
        www.silverbirchhvac.com
      </span>
    </div>
  </section>
</body>
</html>
```